Sign Design for Truck Repair Shop center

Need a road-side sign for a pickup truck repair shop called HaulPoint Garage. The logo is attached and should be used on the sign. The background should be white and the main part of the logo should take up a large part of the sign so it can be easily read by passing traffic. The sign is 4 feet tall by 8 feet wide. Also need to add the website address" "www.HaulPointGarage-example.com" and "Call/Text 555.382.4607"

```html
<!DOCTYPE html>
<html lang="en">
<head>
<meta charset="utf-8">
<title>HaulPoint Garage – Roadside Sign</title>
<link rel="stylesheet" href="https://fonts.googleapis.com/css2?family=Arvo:wght@700&display=swap">
<style>
  :root {
    --page: #eef0f3;
    --white: #ffffff;
    --brand-blue: #33559c;
    --name-blue: #2f54a3;
    --grey-light: #8a8e94;
    --grey-dark: #6d7075;
  }
  html, body {
    margin: 0;
    width: 1200px;
    height: 1200px;
    overflow: hidden;
    background: var(--page);
  }
  .sign {
    position: absolute;
    left: 40px;
    top: 320px;
    width: 1120px;
    height: 560px;
    background: var(--white);
    box-shadow: 0 6px 24px rgba(0,0,0,0.15);
    overflow: hidden;
  }
  .panel-blue {
    position: absolute;
    left: 580px;
    top: 0;
    width: 540px;
    height: 560px;
    background: var(--brand-blue);
  }
  .decor-band {
    position: absolute;
    left: 440px;
    top: 0;
    width: 140px;
    height: 560px;
    background: linear-gradient(90deg, var(--grey-light), var(--grey-dark) 60%, var(--grey-light));
  }
  .brand-name {
    position: absolute;
    left: 20px;
    top: 200px;
    width: 400px;
    margin: 0;
    text-align: center;
    font-family: "Arvo", serif;
    font-weight: 700;
    color: var(--name-blue);
    line-height: 1.05;
    font-size: 64px;
  }
  .brand-name span { display: block; }
  .contact {
    position: absolute;
    left: 610px;
    top: 150px;
    width: 480px;
    font-family: "Arvo", serif;
    font-weight: 700;
    color: var(--white);
    text-align: right;
    white-space: nowrap;
  }
  .headline {
    margin: 0;
    font-size: 50px;
    line-height: 1;
    letter-spacing: 1px;
  }
  .subhead {
    margin: 8px 0 0;
    font-size: 32px;
    line-height: 1;
    letter-spacing: 1px;
  }
  .phone {
    margin: 20px 0 0;
    font-size: 54px;
    line-height: 1;
    letter-spacing: 1px;
    display: flex;
    align-items: center;
    justify-content: flex-end;
    gap: 10px;
  }
  .phone-icon { width: 44px; height: 44px; flex: none; }
  .website {
    margin: 16px 0 0;
    font-size: 20px;
    line-height: 1;
    letter-spacing: 0.5px;
  }
</style>
</head>
<body>
  <section class="sign" aria-label="HaulPoint Garage roadside sign">
    <div class="panel-blue"></div>
    <div class="decor-band" role="img" aria-label="Large grey gear decoration dividing the white and blue panels"></div>

    <h1 class="brand-name"><span>HaulPoint</span><span>Garage</span></h1>

    <div class="contact">
      <p class="headline">TRUCK REPAIR</p>
      <p class="subhead">SHOP CENTER</p>
      <p class="phone">
        <svg class="phone-icon" viewBox="0 0 48 48" aria-hidden="true">
          <circle cx="24" cy="24" r="23" fill="var(--white)"/>
          <path d="M17 12c1.5-1 3 0 3.8 1.5l2 3.8c.6 1.2.3 2.4-.8 3.2l-1.6 1.2c1 2.6 3.3 5 5.9 6.2l1.3-1.6c.8-1 2-1.3 3.1-.7l3.8 2c1.4.8 2.3 2.3 1.3 3.8-1.3 2-3.4 3.3-5.8 2.7C22.5 36 13.8 27.3 12 19.8c-.6-2.5 2.9-6.6 5-7.8z" fill="var(--brand-blue)"/>
        </svg>
        <span>555.382.4607</span>
      </p>
      <p class="website">www.HaulPointGarage-example.com</p>
    </div>
  </section>
</body>
</html>
```